Audio-Visual & Video Communications Business Requires a Cutting-edge Business Card Design

LinkVessel is a new Audio-Visual & Video Communications company in Cape Town, South Africa that is looking for a cutting-edge business card design. We sell these products to the Corporate, Education & Hospitality markets and will also host an Online Shop for companies and individuals to purchase our products online.

We are already using the following two colours in our logo and draft website. Please incorporate these colours into the design. Please note that our website is still in the design stage if you need to visit it. Green #a0ce4e & Dark Grey #333333.
Updates

Hi,

Please note that I have uploaded our logo in an .eps format.

Target Market(s)

Corporate Companies, Education Institutions & Hospitality Markets

Industry/Entity Type

Business

Requirements
Nice to have
• It would be great if you could incorporate the services that we offer.

1. Consultation & Design
2. Project Management
3. Supply & Installation
4. Onsite Support Personal
5. Online Shop

```html
<!DOCTYPE html>
<html lang="en">
<head>
<meta charset="utf-8">
<title>LinkVessel Business Card</title>
<link href="https://fonts.googleapis.com/css2?family=Maven+Pro:wght@400;500;700&display=swap" rel="stylesheet">
<style>
  :root {
    --green: #a0ce4e;
    --grey-dark: #5c5c5c;
    --grey-text: #555555;
    --white: #ffffff;
    --backdrop: #d9dee0;
  }
  * { box-sizing: border-box; margin: 0; padding: 0; }
  html, body { width: 1200px; height: 960px; overflow: hidden; }
  body {
    background: var(--backdrop);
    font-family: "Maven Pro", "Helvetica Neue", Arial, sans-serif;
    display: flex;
    flex-direction: column;
    align-items: center;
    justify-content: center;
    gap: 60px;
  }
  .card {
    width: 700px;
    height: 400px;
    position: relative;
    box-shadow: 0 6px 18px rgba(0,0,0,0.18);
  }
  .card--front { background: var(--white); color: var(--grey-text); }
  .card--back { background: var(--grey-dark); color: var(--white); }

  .brand {
    position: absolute;
    display: flex;
    align-items: center;
    gap: 12px;
  }
  .brand__dot {
    width: 26px; height: 26px; border-radius: 50%;
    background: var(--green);
  }
  .brand__name { font-weight: 700; letter-spacing: -0.5px; }
  .card--front .brand { top: 92px; right: 44px; }
  .card--front .brand__name { font-size: 44px; color: var(--green); }

  .person { position: absolute; left: 44px; top: 166px; }
  .person__name { font-size: 30px; font-weight: 400; letter-spacing: 1px; text-transform: uppercase; color: #4a4a4a; }
  .person__role { font-size: 19px; margin-top: 2px; }

  .contact { position: absolute; left: 44px; bottom: 56px; font-size: 18px; line-height: 1.35; }
  .contact__label { color: var(--green); margin-right: 6px; }
  .contact__address { margin-top: 16px; }

  .website { position: absolute; right: 44px; bottom: 112px; font-size: 16px; color: var(--green); }

  .card--back .brand { top: 110px; left: 50%; transform: translateX(-50%); }
  .card--back .brand__dot { width: 56px; height: 56px; }
  .card--back .brand__name { font-size: 50px; color: var(--white); }

  .services {
    position: absolute; left: 0; right: 0; top: 250px;
    text-align: center; font-size: 16px; letter-spacing: 1.2px; line-height: 1.25;
  }
  .services__sep { color: var(--green); margin: 0 6px; }
</style>
</head>
<body>
  <section class="card card--front" aria-label="Business card front">
    <div class="brand">
      <span class="brand__dot"></span>
      <span class="brand__name">LinkVessel</span>
    </div>
    <div class="person">
      <p class="person__name">Marla Quinby</p>
      <p class="person__role">Manager</p>
    </div>
    <div class="contact">
      <p><span class="contact__label">t</span>021.555.0147</p>
      <p><span class="contact__label">e</span>support@linkvessel.com</p>
      <p class="contact__address">PO Box 2210, Elmford, Brightwater<br>VIC 3999, Australia.</p>
    </div>
    <p class="website">www.linkvessel.com</p>
  </section>

  <section class="card card--back" aria-label="Business card back">
    <div class="brand">
      <span class="brand__dot"></span>
      <span class="brand__name">LinkVessel</span>
    </div>
    <div class="services">
      <p>Consultation &amp; Design<span class="services__sep">•</span>Project Management<span class="services__sep">•</span>Supply &amp; Installation</p>
      <p>Onsite Support Personal<span class="services__sep">•</span>Online Shop</p>
    </div>
  </section>
</body>
</html>
```